Welding and farication business card

Business name Tbm Welding & Fabrication

I need a business card made for my welding and fabrication business that is bold and stands out. My business is both welding repairs on machinery and anything else you can imagine as well as fabricating new products. i have used this service before and was very happy with the out come of my design logo. i think the card should remain fairly simple and classy but also be bold. I think a black card would best be suited to the talk with my logo on it. i feel the back of the card should just have my logo and the front have my logo email, website and phone number and maybe incorporate a facebook and instagram simple if it can be made look good these arnt a necessity.
I have included both my logo and some business card ideas below

Target Market(s)

Farmers, heavy industry, earthmoving, trucking

Industry/Entity Type

Engineering

Contact Information for Business Card

0438517264
dale@tbmweldingandfabrication.com.au
www.tbmweldingandfabrication.com.au

Colors
33a6d7
0255a3

Requirements
Must have
• Dale Hutchins
my phone number 0438517264
my logo
Preferably a black card desgn
Nice to have
• List of what i do,
Sheds and carports
Ute trays
Stockyards
Trailers
Farm equipment
Stockcrates
Gateways and Entrances
Breakdowns
Maintenance
And lots more!

```html
<!DOCTYPE html>
<html lang="en">
<head>
<meta charset="utf-8">
<title>Tbm Welding &amp; Fabrication – Business Card</title>
<link rel="stylesheet" href="https://fonts.googleapis.com/css2?family=Fira+Sans:wght@400;500&display=swap">
<style>
  :root {
    --page: #ffffff;
    --card: #000000;
    --sky: #33a6d7;
    --royal: #0255a3;
    --ink-light: #ffffff;
    --pattern: #1c1c1c;
  }
  * { margin: 0; padding: 0; box-sizing: border-box; }
  html, body {
    width: 1200px; height: 758px; overflow: hidden;
    background: var(--page);
    font-family: "Fira Sans", sans-serif;
  }
  .card {
    position: absolute; top: 190px;
    width: 532px; height: 380px;
    background: var(--card); overflow: hidden;
  }
  .card--back { left: 52px; }
  .card--front { left: 620px; }

  .torch-pattern {
    position: absolute; left: 0; width: 100%;
    background: linear-gradient(180deg, rgba(40,40,40,0.9), rgba(20,20,20,0.35));
  }
  .card--back .torch-pattern--top { top: 0; height: 76px; }
  .card--back .torch-pattern--bottom { top: 280px; height: 86px;
    background: linear-gradient(0deg, rgba(40,40,40,0.9), rgba(20,20,20,0.35)); }
  .card--front .torch-pattern--top { top: 0; height: 42px; }

  .brand {
    position: absolute; display: flex; align-items: center;
    color: var(--ink-light); font-weight: 500;
  }
  .brand__dot { border-radius: 50%; background: var(--sky); flex: none; }
  .brand__name { line-height: 1.05; }
  .brand__name span { display: block; }

  .card--back .brand { left: 0; width: 100%; top: 140px; justify-content: center; gap: 16px; }
  .card--back .brand__dot { width: 26px; height: 26px; }
  .card--back .brand__initials { font-size: 58px; letter-spacing: 4px; }
  .card--back .brand__tag { font-size: 22px; letter-spacing: 0.5px; }

  .card--front .brand { left: 334px; top: 66px; gap: 8px; }
  .card--front .brand__dot { width: 12px; height: 12px; }
  .card--front .brand__initials { font-size: 32px; letter-spacing: 2px; }
  .card--front .brand__tag { font-size: 11.5px; }

  .holder__name {
    position: absolute; left: 46px; top: 78px;
    color: var(--ink-light); font-weight: 500;
    font-size: 32px; letter-spacing: 3.5px; text-transform: uppercase;
  }
  .holder__role {
    position: absolute; left: 46px; top: 112px;
    color: var(--sky); font-size: 15px; letter-spacing: 0.8px;
  }
  .torch-art {
    position: absolute; left: 400px; top: 126px; width: 132px; height: 146px;
    background: radial-gradient(circle at 35% 35%, rgba(255,255,255,0.55), rgba(255,255,255,0.08) 70%, transparent);
  }
  .contact { position: absolute; left: 48px; top: 185px; list-style: none; }
  .contact__item {
    display: flex; align-items: center; gap: 7px; height: 20px;
    color: var(--ink-light); font-size: 15px; letter-spacing: 1px;
  }
  .contact__icon { width: 13px; height: 13px; flex: none; }
  .services {
    position: absolute; left: 0; top: 272px; width: 100%; height: 108px;
    background: var(--sky); color: var(--ink-light);
    padding: 19px 0 0 29px;
    font-size: 14.5px; letter-spacing: 0.6px; line-height: 17.5px;
  }
</style>
</head>
<body>
  <section class="card card--back" aria-label="Card back">
    <div class="torch-pattern torch-pattern--top" role="img" aria-label="Faint repeating pattern of welding torches and sparks"></div>
    <div class="brand">
      <span class="brand__dot"></span>
      <div class="brand__name"><span class="brand__initials">TBM</span><span class="brand__tag">Welding &amp; Fabrication</span></div>
    </div>
    <div class="torch-pattern torch-pattern--bottom" role="img" aria-label="Faint repeating pattern of welding torches and sparks"></div>
  </section>

  <section class="card card--front" aria-label="Card front">
    <div class="torch-pattern torch-pattern--top" role="img" aria-label="Faint repeating pattern of welding sparks"></div>
    <h1 class="holder__name">Dale Hutchins</h1>
    <p class="holder__role">Managing Director</p>
    <div class="brand">
      <span class="brand__dot"></span>
      <div class="brand__name"><span class="brand__initials">TBM</span><span class="brand__tag">Welding &amp; Fabrication</span></div>
    </div>
    <div class="torch-art" role="img" aria-label="White welding torch with a bright spark"></div>
    <ul class="contact">
      <li class="contact__item">
        <svg class="contact__icon" viewBox="0 0 16 16"><path fill="#33a6d7" d="M3.6 1.2 6 3.6 4.7 5.6c.9 2.2 2.5 3.8 4.7 4.7l2-1.3 2.4 2.4-1.6 2.6C6.5 13.8 1.2 8.5 1 2.8z"/></svg>
        0438517264
      </li>
      <li class="contact__item">
        <svg class="contact__icon" viewBox="0 0 16 16"><rect x="1" y="3" width="14" height="10" fill="none" stroke="#33a6d7" stroke-width="1.3"/><path d="M1 3.5 8 9l7-5.5" fill="none" stroke="#33a6d7" stroke-width="1.3"/></svg>
        dale@tbmweldingandfabrication.com.au
      </li>
      <li class="contact__item">
        <svg class="contact__icon" viewBox="0 0 16 16"><g fill="none" stroke="#33a6d7" stroke-width="1.2"><circle cx="8" cy="8" r="6.8"/><ellipse cx="8" cy="8" rx="3" ry="6.8"/><path d="M1.2 8h13.6M2.2 4.6h11.6M2.2 11.4h11.6"/></g></svg>
        www.tbmweldingandfabrication.com.au
      </li>
    </ul>
    <div class="services">
      Sheds | Ute trays | Cattle and sheep yards | Trailers | Farm equipment<br>
      Gateways and Entrances | Breakdowns | Maintenance | And lots more!
    </div>
  </section>
</body>
</html>
```